Website for Private Psychologist

DO NOT CONTACT ME PRIVATELY

I am a Psychologist offering psychotherapy for individuals and couples, and clinical consultation and training and education for mental and medical health professionals and agencies.

I need a redesign of my website

5 Pages (content is attached for each page)
Home
Jungian Psychotherapy
Clinical Consultation & Professional Development
Curriculum Vitae & Publications
Practice Policies and Forms

Designs can be based on these style websites
https://lqmindcare.info; https://pdtarn.org/; https://dorabellcroftcounselling.com/

Design Concepts
Minimalist Layout: Clean and uncluttered layout with generous white space, allowing the content and visuals to stand out'

Keep a linear, uncluttered, professional design.

Please use only royalty free images and google fonts. Please provide links to any stock images used to verify license.

Target Market(s)

private individual or couples seeking psychotherapy

Industry/Entity Type

Psychotherapy

Number of Pages Required

5+ page

Requirements
Should not have
• No search feature

```html
<!DOCTYPE html>
<html lang="en">
<head>
<meta charset="utf-8">
<title>Daniel Whitcombe, Psy.D. — Private Psychologist</title>
<link href="https://fonts.googleapis.com/css2?family=Roboto:wght@400;500;700&display=swap" rel="stylesheet">
<style>
:root{
  --dark:#1d272c;
  --blue:#0563a8;
  --green:#1e8a4e;
  --green-light:#2bb24c;
  --grey:#f4f4f4;
  --ink:#222;
  --muted:#555;
  --white:#fff;
}
*{margin:0;padding:0;box-sizing:border-box}
html,body{width:1200px;height:4819px;overflow:hidden}
body{position:relative;font-family:"Roboto",Arial,sans-serif;color:var(--ink);background:var(--white)}
.abs{position:absolute}
/* top bar */
.topbar{left:0;top:0;width:1200px;height:79px;background:var(--dark);color:var(--white)}
.brand{left:110px;top:28px;font-size:20px;font-weight:700}
.contact-chip{top:18px;display:flex;gap:14px;align-items:center}
.chip-icon{width:36px;height:36px;border-radius:50%;background:var(--green);display:flex;align-items:center;justify-content:center}
.chip-label{font-size:13px;font-weight:500}
.chip-value{font-size:21px;font-weight:500}
/* nav */
.nav{left:0;top:79px;width:1200px;height:52px;background:var(--blue);display:flex;padding-left:80px}
.nav a{color:var(--white);text-decoration:none;font-size:13.5px;font-weight:700;padding:0 13px;line-height:52px}
.nav a.active{background:var(--green)}
/* hero */
.hero{left:0;top:131px;width:1200px;height:640px;background:linear-gradient(90deg,#1f2a2f 0%,#2a3438 40%,#4b5558 70%,#3a4548 100%)}
.hero-visual{left:440px;top:0;width:760px;height:640px;background:radial-gradient(ellipse at 55% 45%,#9fc6d8 0%,#8aa9b0 25%,#6e7a7c 50%,rgba(60,70,72,0) 75%)}
.hero-title{left:108px;top:135px;font-size:43px;font-weight:700;color:var(--white);line-height:1.2}
.hero-sub{left:108px;top:250px;font-size:21px;font-weight:500;color:var(--green-light)}
.btn{display:inline-block;background:var(--blue);color:var(--white);font-weight:700;font-size:13.5px;text-transform:uppercase;border-radius:30px;text-align:center}
.hero-btn{left:108px;top:296px;width:162px;height:42px;line-height:42px}
.dots{left:112px;top:480px;display:flex;gap:8px}
.dots span{width:12px;height:12px;border-radius:50%;background:var(--white)}
.dots span:first-child{background:var(--green-light)}
.hero-wave{left:0;top:560px}
/* headings */
.sec-title{width:1200px;left:0;text-align:center;font-size:40px;font-weight:500;color:var(--ink)}
.underline{left:563px;width:74px;height:3px;background:var(--green)}
/* specializations */
.spec{width:270px;text-align:center}
.spec-photo{position:relative;width:270px;height:270px;border-radius:50%;border:3px solid #d8ece0;padding:7px}
.spec-photo .fill{width:100%;height:100%;border-radius:50%;background:linear-gradient(160deg,#d9d3cb,#9aa2a6 60%,#5d6a70)}
.spec-icon{position:absolute;left:85px;bottom:-20px;width:100px;height:100px;border-radius:50%;background:var(--white);display:flex;align-items:center;justify-content:center}
.spec h3{margin-top:34px;font-size:17px;font-weight:500;line-height:1.5}
.spec p{margin-top:12px;font-size:13px;line-height:1.6;color:var(--muted);padding:0 35px}
.arrow-btn{width:34px;height:34px;border-radius:50%;background:var(--blue);display:flex;align-items:center;justify-content:center}
/* about */
.about{left:0;top:1460px;width:1200px;height:525px;background:var(--green);color:var(--white)}
.about h2{font-size:34px;font-weight:700}
.about .lic{font-size:16px;margin-top:8px}
.about h3{font-size:20px;font-weight:700;margin-top:22px}
.about p{font-size:13.5px;line-height:1.9;text-align:justify;margin-top:12px}
.grey{left:0;top:1985px;width:1200px;height:642px;background:var(--grey)}
.portrait-ring{left:609px;top:1571px;width:508px;height:508px;border-radius:50%;border:4px solid var(--white);background:var(--green)}
.portrait{left:638px;top:1600px;width:450px;height:450px;border-radius:50%;background:linear-gradient(150deg,#c9b7a2,#8a7566 55%,#3b332f)}
.card{left:215px;top:2224px;width:768px;height:266px;background:var(--white);border-radius:14px;box-shadow:0 6px 24px rgba(0,0,0,.08);text-align:center;padding:40px 64px 0}
.card p{font-size:13.5px;line-height:1.6;color:var(--muted);text-align:justify;text-align-last:center}
.card .btn{margin-top:28px;width:440px;height:42px;line-height:42px;font-size:13.5px}
/* feature bands */
.band{left:0;width:1200px;color:var(--white)}
.band-blue{top:2627px;height:481px;background:var(--blue)}
.band-green{top:3108px;height:548px;background:var(--green)}
.round-photo{width:450px;height:450px;border-radius:50%}
.band h2{font-size:40px;font-weight:700;line-height:1.3}
.band .rule{width:64px;height:2px;background:var(--white);margin:24px 0 28px}
.band p{font-size:13.5px;line-height:1.9;text-align:justify}
/* quote form */
.field{border:1px solid #cfcfcf;border-radius:3px;background:var(--white);font-size:13.5px;color:#444;padding:18px 26px}
.submit{left:519px;top:4223px;width:157px;height:40px;line-height:40px}
/* footer */
.footer{left:0;top:4418px;width:1200px;height:401px}
.footer-text{color:var(--white)}
.footer h4{font-size:20px;font-weight:700}
.footer p,.footer li{font-size:13.5px;line-height:1.6}
.footer ul{list-style:none;margin-top:20px}
.footer li{display:flex;gap:10px;margin-bottom:2px}
.copy{left:0;top:4764px;width:1200px;text-align:center;font-size:13.5px;color:var(--white)}
</style>
</head>
<body>

<header class="abs topbar">
  <div class="abs brand">Daniel Whitcombe, Psy.D.</div>
  <div class="abs contact-chip" style="left:518px">
    <div class="chip-icon"><svg width="16" height="12" viewBox="0 0 16 12"><rect x="0" y="0" width="16" height="12" rx="1" fill="#fff"/><path d="M0 1l8 6 8-6" stroke="#1e8a4e" stroke-width="1.6" fill="none"/></svg></div>
    <div><div class="chip-label">Call us Today</div><div class="chip-value">dwhitcombe@mailvault.com</div></div>
  </div>
  <div class="abs contact-chip" style="left:890px">
    <div class="chip-icon"><svg width="16" height="16" viewBox="0 0 24 24"><path fill="#fff" d="M6.6 10.8a15.1 15.1 0 006.6 6.6l2.2-2.2c.3-.3.7-.4 1-.2 1.1.4 2.3.6 3.6.6.6 0 1 .4 1 1V20c0 .6-.4 1-1 1A17 17 0 013 4c0-.6.4-1 1-1h3.5c.6 0 1 .4 1 1 0 1.3.2 2.5.6 3.6.1.3 0 .7-.2 1z"/></svg></div>
    <div><div class="chip-label">Call us Today</div><div class="chip-value">(415) 555-0186</div></div>
  </div>
</header>

<nav class="abs nav">
  <a class="active" href="#">Home</a>
  <a href="#">Jungian Psychotherapy</a>
  <a href="#">Clinical Consultation &amp; Professional Development</a>
  <a href="#">Curriculum Vitae &amp; Publications</a>
  <a href="#">Practice Policies and Forms</a>
</nav>

<section class="abs hero">
  <div class="abs hero-visual" role="img" aria-label="Surreal artwork of a head silhouette opening onto a figure on steps facing the sea"></div>
  <h1 class="abs hero-title">Daniel<br>Whitcombe, Psy.D.</h1>
  <div class="abs hero-sub">Private Psychologist</div>
  <a class="abs btn hero-btn" href="#">Get Started</a>
  <div class="abs dots"><span></span><span></span><span></span><span></span></div>
  <svg class="abs hero-wave" width="1200" height="82" viewBox="0 0 1200 82" preserveAspectRatio="none"><path d="M0 50 C200 0 420 10 640 40 C850 70 1050 80 1200 20 L1200 82 L0 82Z" fill="#fff"/></svg>
</section>

<h2 class="abs sec-title" style="top:866px">Specializations</h2>
<div class="abs underline" style="top:934px"></div>

<div class="abs arrow-btn" style="left:39px;top:1119px"><svg width="16" height="16" viewBox="0 0 16 16"><path d="M14 8H3M7 3L2 8l5 5" stroke="#fff" stroke-width="2.2" fill="none"/></svg></div>
<div class="abs arrow-btn" style="left:1127px;top:1119px"><svg width="16" height="16" viewBox="0 0 16 16"><path d="M2 8h11M9 3l5 5-5 5" stroke="#fff" stroke-width="2.2" fill="none"/></svg></div>

<div class="abs spec" style="left:139px;top:966px">
  <div class="spec-photo"><div class="fill" role="img" aria-label="Photo of a therapy session with a client and therapist seated on a sofa"></div>
    <div class="spec-icon"><svg width="52" height="52" viewBox="0 0 52 52" fill="none" stroke="#1e8a4e" stroke-width="2"><circle cx="26" cy="22" r="14"/><path d="M18 36v10h16V36"/><circle cx="26" cy="22" r="5"/></svg></div></div>
  <h3>Psychotherapy for<br>Individuals and Couples</h3>
  <p>Lorem ipsum dolor sit amet, consectetur adipiscing elit, sed do eiusmod</p>
</div>
<div class="abs spec" style="left:465px;top:966px">
  <div class="spec-photo"><div class="fill" role="img" aria-label="Photo of a smiling consultant talking with a colleague in an office"></div>
    <div class="spec-icon"><svg width="52" height="52" viewBox="0 0 52 52" fill="none" stroke="#1e8a4e" stroke-width="2"><rect x="8" y="10" width="36" height="26" rx="2"/><path d="M20 42h12M26 36v6M14 24h8l3-6 4 12 3-6h6"/></svg></div></div>
  <h3>Clinical Consultation</h3>
  <p>Lorem ipsum dolor sit amet, consectetur adipiscing elit, sed do eiusmod</p>
</div>
<div class="abs spec" style="left:790px;top:966px">
  <div class="spec-photo"><div class="fill" role="img" aria-label="Photo of a trainer presenting to a seated group"></div>
    <div class="spec-icon"><svg width="52" height="52" viewBox="0 0 52 52" fill="none" stroke="#1e8a4e" stroke-width="2"><circle cx="14" cy="16" r="5"/><circle cx="38" cy="16" r="5"/><path d="M6 40v-8a8 8 0 0116 0v8M30 40v-8a8 8 0 0116 0v8M20 44h12"/></svg></div></div>
  <h3>Training and Education<br>for Mental</h3>
  <p>Lorem ipsum dolor sit amet, consectetur adipiscing elit, sed do eiusmod</p>
</div>

<section class="abs about">
  <div class="abs" style="left:110px;top:82px;width:428px">
    <h2>Daniel Whitcombe, Psy.D.</h2>
    <div class="lic">California Licensed Psychologist PSY 48120</div>
    <h3>Jungian Psychotherapy &amp; Consultation</h3>
    <p>I am a California Licensed Psychologist with an office in the San Francisco Financial District offering psychotherapy for individuals and couples, and clinical consultation and training and education for mental and medical health professionals and agencies. All appointments are currently available via telehealth.</p>
    <div style="display:flex;gap:36px;margin-top:16px">
      <div><div style="font-size:15.5px;line-height:1.4;width:192px">For an initial consultation please call:</div><div style="font-size:20px;font-weight:500;margin-top:8px">(415) 555-0186</div></div>
      <div><div style="font-size:15.5px;line-height:1.4">or email:</div><div style="font-size:18px;font-weight:500;margin-top:30px">dwhitcombe@mailvault.com</div></div>
    </div>
  </div>
</section>
<div class="abs grey"></div>
<div class="abs portrait-ring"></div>
<div class="abs portrait" role="img" aria-label="Portrait photo of the psychologist"></div>

<h2 class="abs sec-title" style="top:2118px">My Approach</h2>
<div class="abs card">
  <p>Lorem ipsum dolor sit amet, consectetur adipiscing elit, sed do eiusmod tempor incididunt ut labore et dolore magna aliqua. Ut enim ad minim veniam, quis nostrud exercitation ullamco laboris nisi ut aliquip ex ea commodo consequat. Duis aute irure dolor in reprehenderit in voluptate velit esse cillum dolore eu fugiat nulla pariatur. Excepteur sint occaecat cupidatat non proident, sunt in culpa qui officia deserunt mollit anim id est laborum.</p>
  <a class="btn" href="#">Learn more about my approach and education.</a>
</div>

<section class="abs band band-blue">
  <div class="abs round-photo" style="left:118px;top:113px;background:linear-gradient(160deg,#e8e4dc,#b8a48a 55%,#5a4a3a)" role="img" aria-label="Photo of a therapy room with two armchairs and a lamp"></div>
  <div class="abs" style="left:636px;top:105px;width:452px">
    <h2>Jungian Psychotherapy</h2>
    <div class="rule"></div>
    <p>I practice depth-oriented psychotherapy and tailor my approach to the individual or couple seeking treatment. I have experience treating a range of psychological issues including depression, anxiety, and relationship and job dissatisfaction as well as life transition issues such as college and graduate school stress, pre-marital counseling, and issues related to identity and sexuality.</p>
  </div>
</section>

<section class="abs band band-green">
  <div class="abs" style="left:110px;top:148px;width:520px">
    <h2>Clinical Consultation &amp;<br>Professional Development</h2>
    <div class="rule"></div>
    <p style="width:452px">I provide professional consultation for pre- and post-licensed psychotherapists on a range of clinical issues including substance use disorder assessment and treatment; motivational interviewing; and treatment issues specific to LGBT clients. For Psychology Interns and trainees I offer clinical supervision, case consultation, and professional development.</p>
  </div>
  <div class="abs round-photo" style="left:636px;top:158px;background:linear-gradient(160deg,#f0ece6,#9a7b5a 55%,#3e2f24)" role="img" aria-label="Photo of an office with a wooden desk and tall bookshelf"></div>
</section>

<h2 class="abs sec-title" style="top:3782px">Get A Quote</h2>
<div class="abs field" style="left:225px;top:3890px;width:357px;height:52px">First name</div>
<div class="abs field" style="left:612px;top:3890px;width:358px;height:52px">Last name</div>
<div class="abs field" style="left:225px;top:3959px;width:357px;height:51px">Email</div>
<div class="abs field" style="left:612px;top:3959px;width:358px;height:51px">Phone</div>
<div class="abs field" style="left:225px;top:4027px;width:745px;height:172px">Message</div>
<a class="abs btn submit" href="#">Submit Now</a>

<footer class="abs footer">
  <svg class="abs" style="left:0;top:0" width="1200" height="401" viewBox="0 0 1200 401" preserveAspectRatio="none"><path d="M0 40 C180 -10 380 0 560 30 C780 65 1000 60 1200 15 L1200 401 L0 401Z" fill="#1d272c"/></svg>
  <div class="abs footer-text" style="left:110px;top:125px;width:320px">
    <h4>Daniel Whitcombe, Psy.D.</h4>
    <p style="margin-top:18px">California Licensed Psychologist PSY 48120</p>
    <p style="margin-top:16px">Lorem ipsum dolor sit amet, consectetur adipisc ing elit, sed do eiusmod tempor incididunt ut labore et dolore magna aliqua.</p>
  </div>
  <div class="abs footer-text" style="left:513px;top:125px;width:270px">
    <h4>Quick Links</h4>
    <ul>
      <li><svg width="14" height="14" viewBox="0 0 14 14"><path d="M2 7l3 3 7-7" stroke="#2bb24c" stroke-width="2" fill="none"/></svg>Home</li>
      <li><svg width="14" height="14" viewBox="0 0 14 14"><path d="M2 7l3 3 7-7" stroke="#2bb24c" stroke-width="2" fill="none"/></svg>Jungian Psychotherapy</li>
      <li><svg width="14" height="14" viewBox="0 0 14 14" style="flex:none"><path d="M2 7l3 3 7-7" stroke="#2bb24c" stroke-width="2" fill="none"/></svg>Clinical Consultation &amp; Professional Development</li>
      <li><svg width="14" height="14" viewBox="0 0 14 14"><path d="M2 7l3 3 7-7" stroke="#2bb24c" stroke-width="2" fill="none"/></svg>Curriculum Vitae &amp; Publications</li>
      <li><svg width="14" height="14" viewBox="0 0 14 14"><path d="M2 7l3 3 7-7" stroke="#2bb24c" stroke-width="2" fill="none"/></svg>Practice Policies and Forms</li>
    </ul>
  </div>
  <div class="abs footer-text" style="left:852px;top:125px;width:250px">
    <h4>Contact Us</h4>
    <ul>
      <li><svg width="12" height="16" viewBox="0 0 12 16" style="flex:none"><path d="M6 0a6 6 0 016 6c0 4.5-6 10-6 10S0 10.5 0 6a6 6 0 016-6z" fill="#2bb24c"/><circle cx="6" cy="6" r="2.2" fill="#1d272c"/></svg>California Licensed Psychologist PSY 48120</li>
      <li style="margin-top:18px"><svg width="14" height="14" viewBox="0 0 24 24"><path fill="#2bb24c" d="M6.6 10.8a15.1 15.1 0 006.6 6.6l2.2-2.2c.3-.3.7-.4 1-.2 1.1.4 2.3.6 3.6.6.6 0 1 .4 1 1V20c0 .6-.4 1-1 1A17 17 0 013 4c0-.6.4-1 1-1h3.5c.6 0 1 .4 1 1 0 1.3.2 2.5.6 3.6.1.3 0 .7-.2 1z"/></svg>(415) 555-0186</li>
      <li style="margin-top:18px"><svg width="14" height="12" viewBox="0 0 16 12"><rect width="16" height="12" rx="1" fill="#2bb24c"/><path d="M0 1l8 6 8-6" stroke="#1d272c" stroke-width="1.4" fill="none"/></svg>dwhitcombe@mailvault.com</li>
    </ul>
  </div>
</footer>
<div class="abs" style="left:0;top:4745px;width:1200px;height:1px;background:rgba(255,255,255,.12)"></div>
<div class="abs copy">© Copyrights 2023 | All Rights Reserved</div>

</body>
</html>
```